Web site - 5-8 page

We are a small, fresh pasta business called The Noodle Lark located in suburbs of Sacramento, CA. We sell our pasta, ravioli, meatballs and sauce at farmer's markets, events, and soon in our café & marketplace. (Jan 2014) . We also provide catering services. The site needs to communicate FRESH, local, no preservatives, artisan quality pasta. We offer vegetarian, vegan and gluten free products as well.

We would like a web site using our logos and colors to feature what we do, and where people can come buy it. A page to our standard take and make items/menu, our seasonal take and make menu, our catering menu, our new hot food café menu.

We want a page that we can update with "Where can you find The Noodle Lark"
A "specials page" and a page they can order from that they choose the location to pick it up or in the delivery area we deliver to them.
A page with photo's and referrals, testimony, comments, about us, etc. Maybe a page for recipes.
We need to update the events/find us page all the time, weekly, so it needs to be easy for us to go in and do that. We are Window's (not MAC) users if that makes a difference or not, not sure.

Ideally, the same person(s) that make the website would also do a separate project creating our catering and hot food menu brochure/layout and recipe cards

Reason: allow enough time for good quality work

I would like to see the landing page have the pasta shapes/sizes element that is found in the refrigerator wrap, the wrap on the trailer, and the menu - see photo and uploads. It's used as a banner or as a background, bright green.

                                   

 

Would like visitors to be able to "like" me or follow me from my web page. A button or a link?

                                        http://www.brightpantry-example.com/our-food/

Really like the layout of this site. More grocery oriented than café, but we are a take and make marketplace as well as a Panini salads and hot pasta menu for lunch.

Please add Café + Marketplace to headers. Our logo is good but we are now adding a café element and a fresh marketplace, se we need to communicate what we are/what we do. We think adding Café + Marketplace as a descriptor will help. Any ideas, feel free to put your own spin on it. Thank you!!

The designs are good...thanks to everyone!

Reason: To allow for the many updates we have added. Good designs coming in, thank you!

Target Market(s)

#1, busy mom's, busy family's (FAST, Economical meals, no preservatives, local food)
#2 24-34 yr olds that want fresh, vegetarian, vegan or gluten free meal options (no preservatives, local food)
#3 Fresh pasta lovers - any age. The enjoyment of quality fresh pasta and a good meal experience sharing it with friends and family

Industry/Entity Type

Catering

Font styles to use
Other font styles liked:
• EideticNeoRegular, duffy

Colors
9bcb3c
f78f20
eb1f27

Requirements
Must have
• Address, phone, name, logo, colors
Fresh pasta, ravioli, sauce and meatballs in take and make convenient packages. Stress fresh, preservative free, local ingredients, cooks in 45 SECONDS to 3.5 minutes depending on the pasta cut.
FAST meal
Where to find us page - upcoming events
A "specials" page
A page for recipe, how to cook our pasta, how to freeze and store fresh pasta,
How to order online page
Nice to have
• Testimony, links to Facebook, twitter, etc. Place for photo's of product, recent events, customer comments on how they used the product to create their recipe.
Should not have
• No stock photo's of tomato's, no dried pasta images, no Italian flags. No cheesy old world Italian loo or feel. Think fresh, modern, FAST!

```html
<!DOCTYPE html>
<html lang="en">
<head>
<meta charset="utf-8">
<title>The Noodle Lark – Café + Marketplace</title>
<link rel="stylesheet" href="https://fonts.googleapis.com/css2?family=Roboto+Condensed:wght@400;700&family=PT+Sans:wght@400;700&family=Kaushan+Script&display=swap">
<style>
:root{
  --orange-bar:#f0522f;
  --orange-nav:#d63b1e;
  --logo-dark:#2a2a2a;
  --green:#8aba2a;
  --green-btn:#a8cf2f;
  --orange:#f5901f;
  --orange-btn:#e4700f;
  --red:#eb1f27;
  --red-btn:#c8101a;
  --yellow:#fff200;
  --cream:#fdefc1;
  --sand:#f1dc9f;
  --white:#ffffff;
  --title-red:#e0291b;
}
*{box-sizing:border-box;margin:0;padding:0}
html,body{width:1155px;height:1200px;overflow:hidden}
body{position:relative;background:var(--cream);font-family:"Roboto Condensed",sans-serif;color:var(--white)}
a{color:inherit;text-decoration:none}

.topbar{position:absolute;left:0;top:0;width:1155px;height:56px;background:var(--orange-bar)}
.topbar .brand-name{position:absolute;left:533px;top:20px;font:700 12.5px "PT Sans",sans-serif;letter-spacing:.2px}
.topbar .divider{position:absolute;top:0;width:1px;height:56px;background:rgba(0,0,0,.12)}
.topbar .address{position:absolute;left:691px;top:13px;font:400 11px/18px "PT Sans",sans-serif}
.topbar .phone{position:absolute;left:922px;top:13px;font:400 11px/18px "PT Sans",sans-serif}
.topbar .phone-icon{position:absolute;left:885px;top:17px}

.mainnav{position:absolute;left:0;top:56px;width:1155px;height:50px;background:var(--orange-nav)}
.mainnav ul{position:absolute;left:349px;top:19px;display:flex;gap:28px;list-style:none;font-size:11px;text-transform:uppercase}

.logo{position:absolute;left:165px;top:0;width:160px;height:181px;background:var(--logo-dark);border:1px solid #555;outline:4px solid var(--logo-dark);outline-offset:-5px;display:flex;flex-direction:column;align-items:center;justify-content:center;gap:10px;z-index:3}
.logo .mark{width:14px;height:14px;background:var(--orange-bar)}
.logo .name{font:700 17px "Roboto Condensed",sans-serif;color:var(--orange-bar);text-transform:uppercase;text-align:center;line-height:20px}

.hero{position:absolute;left:0;top:106px;width:1155px;height:491px;overflow:hidden;
  background:
    radial-gradient(ellipse 470px 250px at 600px 230px,#f6e39a 0%,#f1d574 45%,#e8c65a 70%,rgba(232,198,90,0) 100%),
    radial-gradient(ellipse 600px 330px at 590px 260px,#f3efe4 0%,#f3efe4 86%,rgba(243,239,228,0) 100%),
    radial-gradient(ellipse 640px 360px at 590px 250px,#d9584a 0%,#d9584a 90%,rgba(217,88,74,0) 100%),
    radial-gradient(circle 70px at 1080px 30px,#e6ef3a 0%,rgba(230,239,58,0) 100%),
    linear-gradient(180deg,#c9a77e 0%,#e2c7a0 60%,#d9b98f 100%)}
.hero .arrow{position:absolute;top:214px;width:58px;height:58px;border:2px solid rgba(255,255,255,.55);border-radius:50%}
.hero .arrow.prev{left:56px}
.hero .arrow.next{left:1030px}
.hero .arrow svg{position:absolute;left:13px;top:14px}
.hero .tagline{position:absolute;left:185px;top:326px;font-family:"Kaushan Script",cursive;color:var(--red);line-height:1;font-weight:400}
.hero .tagline .l1{display:block;font-size:32px}
.hero .tagline .l2{display:block;font-size:44px;margin-top:12px}

.features{position:absolute;left:0;top:597px;width:1155px;height:224px;background:var(--sand)}
.panel{position:absolute;top:0;width:276px;height:224px}
.panel.testimonial{left:165px;background:var(--green)}
.panel.comments{left:441px;background:var(--orange)}
.panel.events{left:717px;background:var(--red)}
.panel h2{position:absolute;left:28px;top:26px;font-size:19px;font-weight:400;letter-spacing:-.2px;text-transform:uppercase;white-space:nowrap}
.panel .pager{position:absolute;right:24px;top:28px;font-size:14px;letter-spacing:5px;color:rgba(255,255,255,.85)}
.panel h3{position:absolute;top:66px;font-size:14px;font-weight:400;color:var(--yellow);text-transform:uppercase}
.panel p{position:absolute;font-size:10.2px;line-height:18px;text-transform:uppercase}
.panel .photo{position:absolute;left:20px;top:62px;width:96px;height:96px;border-radius:50%;border:2px solid rgba(255,255,255,.7)}
.panel .btn{position:absolute;left:28px;top:177px;padding:2px 12px;font-size:16px;text-transform:uppercase}
.testimonial h3{left:28px}
.testimonial p{left:28px;top:88px;width:215px}
.testimonial .btn{background:var(--green-btn)}
.comments h3,.events h3{left:136px}
.comments p,.events p{left:136px;top:84px;width:128px}
.comments .btn{background:var(--orange-btn);left:30px}
.events .btn{background:var(--red-btn);left:28px}
.comments .photo{background:radial-gradient(circle at 50% 42%,#f3dcc4 0%,#e2bb94 35%,#caa27a 55%,#8fc3e0 75%,#b9dcef 100%)}
.events .photo{background:radial-gradient(circle at 45% 45%,#e4b060 0%,#c86a33 30%,#a33a22 55%,#5f6f2e 80%,#3e3a2a 100%)}

.products{position:absolute;left:165px;top:821px;width:826px}
.products h2{position:absolute;left:2px;top:31px;font-size:20px;font-weight:400;color:var(--title-red);text-transform:uppercase}
.products .pager{position:absolute;right:2px;top:33px;font-size:14px;letter-spacing:5px;color:#9a8b66}
.tile{position:absolute;top:72px;width:192px;height:179px;border:3px solid #f5e3a6}
.tile:nth-of-type(1){left:0}
.tile:nth-of-type(2){left:211px}
.tile:nth-of-type(3){left:422px}
.tile:nth-of-type(4){left:633px}
.tile.featured{background:radial-gradient(ellipse at 50% 35%,#b7d86a 0%,#9ac63f 55%,#8cbd33 100%)}
.tile.featured .label{position:absolute;left:27px;top:106px;text-transform:uppercase}
.tile.featured .label strong{display:block;font-size:20px;font-weight:400}
.tile.featured .label span{display:block;font-size:14px;margin-top:4px}
.tile.fusilli{background:
    radial-gradient(ellipse 70px 55px at 95px 90px,#e2b25a 0%,#d79e3e 60%,rgba(215,158,62,0) 100%),
    radial-gradient(ellipse 95px 80px at 95px 85px,#f5f2ea 0%,#f5f2ea 85%,rgba(245,242,234,0) 100%),
    linear-gradient(160deg,#e7cf9a 0%,#dcb46a 100%)}
.tile.spinach{background:
    radial-gradient(circle 45px at 100px 70px,#3f7a2c 0%,#5a8f38 50%,rgba(90,143,56,0) 100%),
    radial-gradient(ellipse 75px 70px at 90px 95px,#d5683a 0%,#c95a30 60%,rgba(201,90,48,0) 100%),
    radial-gradient(circle 92px at 90px 92px,#f4f1ea 0%,#f4f1ea 88%,rgba(244,241,234,0) 100%),
    linear-gradient(135deg,#5c6270 0%,#6d7280 45%,#e48040 70%,#52575f 100%)}
.tile.penne{background:
    radial-gradient(ellipse 70px 45px at 95px 95px,#c7904c 0%,#a86a3a 50%,rgba(168,106,58,0) 100%),
    radial-gradient(ellipse 100px 65px at 95px 100px,#fbfaf7 0%,#f2f1ec 85%,rgba(242,241,236,0) 100%),
    linear-gradient(180deg,#cfd3cc 0%,#9ea39c 60%,#5a5e58 100%)}

.footer{position:absolute;left:0;top:1113px;width:1155px;height:87px;background:var(--orange-bar)}
.footer ul{position:absolute;left:166px;top:25px;display:flex;list-style:none;font-size:10.5px;text-transform:uppercase}
.footer li+li::before{content:"I";margin:0 15px}
.footer .copy{position:absolute;left:166px;top:53px;font-size:10.5px;text-transform:uppercase}
.footer .social{position:absolute;left:880px;top:33px;display:flex;gap:5px}
.footer .social a{width:33px;height:33px;border-radius:50%;background:rgba(0,0,0,.12);display:block}
</style>
</head>
<body>

<header>
  <div class="topbar">
    <span class="brand-name">THE NOODLE LARK</span>
    <span class="divider" style="left:662px"></span>
    <address class="address" style="font-style:normal">4820 Willow Crest Ave. #210,<br>Maple Hollow, CA 95999</address>
    <span class="divider" style="left:860px"></span>
    <svg class="phone-icon" width="24" height="24" viewBox="0 0 24 24" aria-hidden="true">
      <rect x="8" y="2" width="13" height="18" rx="2" fill="none" stroke="#fff" stroke-width="1.6"/>
      <path d="M5 5 v14 a3 3 0 0 0 3 3" fill="none" stroke="#fff" stroke-width="1.6"/>
      <g fill="#fff"><rect x="11" y="5" width="7" height="3"/><circle cx="11.5" cy="11" r="1"/><circle cx="14.5" cy="11" r="1"/><circle cx="17.5" cy="11" r="1"/><circle cx="11.5" cy="14" r="1"/><circle cx="14.5" cy="14" r="1"/><circle cx="17.5" cy="14" r="1"/></g>
    </svg>
    <div class="phone">Call Us:<br>916-555-0148</div>
  </div>

  <a class="logo" href="#">
    <span class="mark"></span>
    <span class="name">The Noodle<br>Lark</span>
  </a>

  <nav class="mainnav">
    <ul>
      <li><a href="#">Home</a></li>
      <li><a href="#">Fast Meal</a></li>
      <li><a href="#">Where to find us page</a></li>
      <li><a href="#">Upcoming Events</a></li>
      <li><a href="#">Specials</a></li>
      <li><a href="#">Recipe</a></li>
      <li><a href="#">Order Online</a></li>
      <li><a href="#">Contact Us</a></li>
    </ul>
  </nav>
</header>

<section class="hero" role="img" aria-label="Bowl of fresh fusilli pasta with chopped chives">
  <a class="arrow prev" href="#" aria-label="Previous slide">
    <svg width="28" height="28" viewBox="0 0 28 28"><path d="M26 2 L2 14 L26 26 L20 14 Z" fill="rgba(255,255,255,.6)"/></svg>
  </a>
  <a class="arrow next" href="#" aria-label="Next slide">
    <svg width="28" height="28" viewBox="0 0 28 28"><path d="M2 2 L26 14 L2 26 L8 14 Z" fill="rgba(255,255,255,.6)"/></svg>
  </a>
  <h1 class="tagline"><span class="l1">Fresh Ready-to-make</span><span class="l2">Pasta,Ravioli &amp; Sauce</span></h1>
</section>

<section class="features">
  <article class="panel testimonial">
    <h2>Testimonial</h2>
    <span class="pager">‹ ›</span>
    <h3>Cooking Fresh Pasta (Noodles)</h3>
    <p>Bring 3 to 4 quarts water to boil. Add one tablespoon kosher salt. Place pasta in water. Stir gently with a pasta fork to separate. Reduce...</p>
    <a class="btn" href="#">Read More</a>
  </article>
  <article class="panel comments">
    <h2>Customer Comments</h2>
    <span class="pager">‹ ›</span>
    <div class="photo" role="img" aria-label="Customer portrait"></div>
    <h3>Lena Marsh</h3>
    <p>Bring 3 to 4 quarts water to boil. Add one tablespoon kosher salt. Place...</p>
    <a class="btn" href="#">Read More</a>
  </article>
  <article class="panel events">
    <h2>Recent Events</h2>
    <span class="pager">‹ ›</span>
    <div class="photo" role="img" aria-label="Plate of pasta with vegetables and a fork"></div>
    <h3>28 Aug 2013</h3>
    <p>Bring 3 to 4 quarts water to boil. Add one tablespoon kosher salt. Place...</p>
    <a class="btn" href="#">Read More</a>
  </article>
</section>

<section class="products">
  <h2>Our Products</h2>
  <span class="pager">‹ ›</span>
  <a class="tile featured" href="#" role="img" aria-label="Conchigliette pasta dish">
    <span class="label"><strong>Conchigliette</strong><span>Click here for large</span></span>
  </a>
  <a class="tile fusilli" href="#" role="img" aria-label="Fusilli with zucchini and cheese on a white plate"></a>
  <a class="tile spinach" href="#" role="img" aria-label="Pasta with spinach and parmesan in a white bowl"></a>
  <a class="tile penne" href="#" role="img" aria-label="Penne with roasted vegetables and basil"></a>
</section>

<footer class="footer">
  <ul>
    <li><a href="#">Home</a></li>
    <li><a href="#">Fast Meal</a></li>
    <li><a href="#">Where to find us page</a></li>
    <li><a href="#">Upcoming Events</a></li>
    <li><a href="#">Specials</a></li>
    <li><a href="#">Recipe</a></li>
    <li><a href="#">Order Online</a></li>
    <li><a href="#">Contact Us</a></li>
  </ul>
  <p class="copy">Copyrights © 2013. The Noodle Lark. All rights reserved.</p>
  <div class="social">
    <a href="#" aria-label="Social profile 1"></a>
    <a href="#" aria-label="Social profile 2"></a>
    <a href="#" aria-label="Social profile 3"></a>
  </div>
</footer>

</body>
</html>
```